Redesign Wordpress website for ultrasound business

We need our Wordpress website redesigned.
We are a small and newly established ultrasound practice in a rural area in NSW, Australia. We specialise in medical/diagnostic and entertainment ultrasound and are the only practice in the region to offer 3D/4D pregnancy ultrasounds without a referral. We offer a wide range of medical ultrasounds for every area of the body.
Unlike most other medical imaging companies, ours is owned by our sonographer (the person doing the scans) rather than a doctor or business person. So the focus of our business is on our patients rather than revenue. We offer weekend and after hours appointments to cater to everyones schedules.
Because we offer medical and entertainment ultrasounds, we have 3 different areas of clientele that we market to...
- Referring Doctors...we need to market to the doctors in the area to get them to refer patients to us.
- Medical ultrasound patients....men, women and children of all ages that need an ultrasound for whatever reason (injury, pregnancy, illness, general checkup). These people are focused more locally
- Pregnant women for entertainment ultrasounds of their babies....because we're the only practice to offer this service without a referral, our clientele is over about a 400km radius

Our current website has been created on Wordpress. It's corvellascans.com.au

We ideally want a website that uses the themes featured in our logo and other stationary. The logo and business card has been included to give you an idea of our styling.
I would appreciate your assistance with imagery for the site though as that is one thing I'm really not happy with at the moment.

The website needs a section specifically for doctors with all the medical information they need about types of ultrasounds we offer as well as the link (currently on our website under "referrers") to login and see their patient's images.
It also needs areas for patients with information about medical ultrasounds (what they are, what happens during the scan and prep for scans) and 3D/4D ultrasounds (what it is, package options).
An area for a blog/news and up-dates is required too. The newsletter signup part isn't necessary.
I would like our facebook feed to be incorporated somehow but only if it doesn't degrade the overall aesthetics of the page.
Links to facebook and instagram is required.

The address is 47 Wattlebrook st Blayney, NSW 2799. An imbedded google map of our location is desired.

Phone: 0263917258
Email: admin@corvellascans.com.au
Facebook: https://www.facebook.com/CorvellaScans/
Instagram: https://www.instagram.com/corvellascans/
ABN: 7318842619

There are some great medical imaging and ultrasound practice websites around for other businesses so in order to design a competitive website, the designer would need research the other websites, their structure, page layouts, images and text wording.

```html
<!DOCTYPE html>
<html lang="en">
<head>
<meta charset="utf-8">
<title>Corvella Scans – 3D/4D Pregnancy Ultrasounds</title>
<link href="https://fonts.googleapis.com/css2?family=Poppins:wght@300;400;500;600;700&display=swap" rel="stylesheet">
<style>
  :root {
    --purple-dark: #6a2670;
    --purple: #8a2d9a;
    --purple-bright: #a232c2;
    --ink: #2b2b2b;
    --ink-soft: #3a3a3a;
    --topbar: #f8f2f7;
    --white: #ffffff;
  }
  * { margin: 0; padding: 0; box-sizing: border-box; }
  html, body { width: 1200px; height: 637px; overflow: hidden; background: var(--white); }
  body { font-family: "Poppins", sans-serif; color: var(--ink); position: relative; }

  .topbar { position: absolute; left: 0; top: 0; width: 1200px; height: 48px; background: var(--topbar); }
  .address { position: absolute; left: 576px; top: 15px; display: flex; align-items: center; gap: 6px; font-size: 14px; color: var(--ink-soft); }
  .contact-call { position: absolute; left: 812px; top: 9px; display: flex; align-items: center; gap: 8px; }
  .contact-call small { display: block; font-size: 11px; letter-spacing: .3px; line-height: 13px; color: var(--ink-soft); }
  .contact-call strong { display: block; font-size: 17px; font-weight: 600; line-height: 20px; color: var(--ink); }
  .social { position: absolute; left: 993px; top: 11px; display: flex; gap: 15px; }
  .social a { display: block; width: 28px; height: 28px; border-radius: 5px; border: 3px solid var(--ink); }
  .social a.facebook { background: var(--ink); }

  .header { position: absolute; left: 0; top: 48px; width: 1200px; height: 80px; background: var(--white); }
  .brand { position: absolute; left: 128px; top: -42px; width: 120px; text-decoration: none; text-align: center; }
  .brand-mark { display: block; width: 70px; height: 70px; margin: 0 auto 6px; border-radius: 50%; border: 4px solid var(--purple); }
  .brand-name { font-size: 16px; font-weight: 500; letter-spacing: 1px; color: var(--purple); line-height: 18px; }

  .nav { position: absolute; left: 362px; top: 0; height: 80px; display: flex; }
  .nav a { position: relative; display: flex; align-items: center; height: 80px; padding: 0 19.5px; font-size: 14.5px; font-weight: 500; color: var(--ink); text-decoration: none; }
  .nav a:first-child { padding-left: 19px; }
  .nav a.active { color: var(--purple); }
  .nav a.active::after { content: ""; position: absolute; left: 0; right: 0; bottom: 0; height: 3px; background: var(--purple); }

  .hero { position: absolute; left: 0; top: 128px; width: 1200px; height: 509px; overflow: hidden; }
  .hero-photo { position: absolute; inset: 0;
    background:
      radial-gradient(ellipse 55% 60% at 50% 55%, rgba(255,255,255,.55), rgba(255,255,255,0) 70%),
      linear-gradient(100deg, #d9d9dc 0%, #e6e4e4 30%, #efe9e6 55%, #f3f1ef 80%, #f7f7f7 100%); }
  .hero-content { position: absolute; left: 0; right: 0; top: 138px; text-align: center; }
  .hero-kicker { font-size: 40px; font-weight: 600; color: #1f1f1f; line-height: 46px; letter-spacing: .3px; }
  .hero-title { font-size: 72px; font-weight: 700; line-height: 80px; margin-top: -2px;
    background: linear-gradient(90deg, var(--purple-dark), var(--purple-bright));
    -webkit-background-clip: text; background-clip: text; color: transparent; }
  .hero-sub { font-size: 25px; font-weight: 300; color: var(--ink-soft); margin-top: 10px; }
  .btn-book { display: inline-block; margin-top: 22px; width: 276px; height: 46px; line-height: 46px; border-radius: 23px;
    background: linear-gradient(90deg, var(--purple-dark), var(--purple-bright)); color: var(--white);
    font-size: 17px; font-weight: 500; text-decoration: none; }
</style>
</head>
<body>
  <div class="topbar">
    <div class="address">
      <svg width="10" height="14" viewBox="0 0 10 14"><path d="M5 0C2.2 0 0 2.2 0 5c0 3.6 5 9 5 9s5-5.4 5-9c0-2.8-2.2-5-5-5zm0 7a2 2 0 1 1 0-4 2 2 0 0 1 0 4z" fill="#2b2b2b"/></svg>
      47 Wattlebrook St, Blayney
    </div>
    <div class="contact-call">
      <svg width="28" height="28" viewBox="0 0 24 24"><path d="M6.6 10.8a15.1 15.1 0 0 0 6.6 6.6l2.2-2.2c.3-.3.7-.4 1-.2 1.1.4 2.3.6 3.6.6.6 0 1 .4 1 1V20c0 .6-.4 1-1 1C10.6 21 3 13.4 3 4c0-.6.4-1 1-1h3.5c.6 0 1 .4 1 1 0 1.3.2 2.5.6 3.6.1.3 0 .7-.2 1L6.6 10.8z" fill="#2b2b2b"/></svg>
      <div><small>HAVE A QUESTION?</small><strong>02 6391 7258</strong></div>
    </div>
    <nav class="social">
      <a class="facebook" href="https://www.facebook.com/CorvellaScans/" aria-label="Facebook"></a>
      <a class="instagram" href="https://www.instagram.com/corvellascans/" aria-label="Instagram"></a>
    </nav>
  </div>

  <header class="header">
    <a class="brand" href="#">
      <span class="brand-mark"></span>
      <span class="brand-name">Corvella Scans</span>
    </a>
    <nav class="nav">
      <a class="active" href="#">HOME</a>
      <a href="#">ABOUT</a>
      <a href="#">SERVICES</a>
      <a href="#">FAQS</a>
      <a href="#">BLOG</a>
      <a href="#">BOOKINGS</a>
      <a href="#">CONTACT</a>
      <a href="#">REFERRERS</a>
    </nav>
  </header>

  <section class="hero">
    <div class="hero-photo" role="img" aria-label="Soft, faded photo of a smiling pregnant woman having an ultrasound scan beside the scanning machine"></div>
    <div class="hero-content">
      <p class="hero-kicker">3D/4D PREGNANCY</p>
      <h1 class="hero-title">ULTRASOUNDS</h1>
      <p class="hero-sub">Diagnostic ultrasound services to the Blayney community</p>
      <a class="btn-book" href="#">BOOK AN APPOINTMENT</a>
    </div>
  </section>
</body>
</html>
```